Marigold Works Flyer - RV Solar and Residential Solar

We would like to create a tri-fold brochure for our company for distribution in the mail. This will advertise our services, products and some references.

Our cover page should include a logo and contact information as well as some solar stock imagery.

Our inside pages should cover residential solar, RV solar and a solar education / facts portion.

The rear pages would be left for our remaining services and some references / testimonials.

Target Market(s)

Residential Homeowners and Recreational Vehicles

Industry/Entity Type

Solar Energy

Font styles to use
Serif
Sans Serif

Requirements
Must have
• Must match the color scheme of our logo.
Nice to have
• Solar stock images for RV solar and residential solar.
Either a black or white background with our logo is eye-catching,

```html
<!DOCTYPE html>
<html lang="en">
<head>
<meta charset="utf-8">
<title>Marigold Works – Solar Brochure Inside Spread</title>
<link rel="stylesheet" href="https://fonts.googleapis.com/css2?family=Montserrat:wght@800&family=Roboto:wght@300;700&family=Roboto+Condensed:wght@700&display=swap">
<style>
  :root {
    --charcoal: #333335;
    --paper: #ffffff;
    --brand-blue: #2a55c4;
    --ink: #2f2f2f;
    --light: #f2f2f2;
    --grey-3: #a9a9a9;
  }
  * { margin: 0; padding: 0; box-sizing: border-box; }
  html, body { width: 1200px; height: 848px; overflow: hidden; background: var(--paper); }
  .spread { position: relative; width: 1200px; height: 848px; overflow: hidden; font-family: "Roboto", sans-serif; font-weight: 300; }
  .panel { position: absolute; top: 0; height: 848px; width: 400px; }
  .panel--residential { left: 0; background: var(--charcoal); }
  .panel--rv { left: 400px; background: var(--paper); }
  .panel--multi { left: 800px; background: var(--charcoal); }

  .art { position: absolute; top: 0; left: 0; }

  .heading { position: absolute; color: var(--brand-blue); font-family: "Montserrat", sans-serif; font-weight: 800; line-height: 0.9; text-align: center; letter-spacing: 0.5px; }
  .heading--residential { left: 50px; width: 345px; top: 383px; font-size: 41px; }
  .heading--rv { left: 415px; width: 376px; top: 300px; font-size: 41px; }
  .heading--facts { left: 415px; width: 372px; top: 580px; font-size: 41px; }
  .heading--multi { left: 864px; top: 424px; font-family: "Roboto Condensed", sans-serif; font-weight: 700; font-size: 35px; line-height: 38px; text-align: left; letter-spacing: 0; }

  .list { position: absolute; list-style: none; font-size: 17px; line-height: 25.7px; }
  .list li { position: relative; padding-left: 25px; }
  .list--arrow li::before { content: ">"; position: absolute; left: 0; font-weight: 300; }
  .list--numbered { counter-reset: step; }
  .list--numbered li { counter-increment: step; padding-left: 25px; }
  .list--numbered li::before { content: counter(step); position: absolute; left: 0; font-weight: 700; }

  .on-dark { color: var(--light); }
  .on-light { color: var(--ink); }

  .list--residential { left: 39px; top: 487px; width: 332px; }
  .list--offers { left: 433px; top: 28px; width: 336px; }
  .list--rv { left: 435px; top: 347px; width: 330px; }
  .list--facts { left: 433px; top: 657px; width: 332px; }
  .list--multi { left: 836px; top: 28px; width: 336px; }
</style>
</head>
<body>
<main class="spread">

  <section class="panel panel--residential"></section>
  <section class="panel panel--rv"></section>
  <section class="panel panel--multi"></section>

  <svg class="art" width="1200" height="848" viewBox="0 0 1200 848" aria-hidden="true">
    <polygon points="0,361 84,361 0,444" fill="var(--grey-3)"/>
  </svg>
  <svg class="art" width="1200" height="848" viewBox="0 0 1200 848" role="img" aria-label="Photo of a tiled house roof fitted with blue solar panels beneath green trees">
    <defs>
      <linearGradient id="roofPhoto" x1="0" y1="0" x2="1" y2="1">
        <stop offset="0" stop-color="#6f8a5a"/>
        <stop offset="0.3" stop-color="#3f6fc4"/>
        <stop offset="0.65" stop-color="#2b4f9e"/>
        <stop offset="1" stop-color="#8a6a55"/>
      </linearGradient>
    </defs>
    <polygon points="0,0 444,0 84,361 0,361" fill="url(#roofPhoto)"/>
  </svg>

  <svg class="art" width="1200" height="848" viewBox="0 0 1200 848" role="img" aria-label="Photo of a worker in a hi-vis vest installing solar panels on ground-mounted racking in a field">
    <defs>
      <linearGradient id="fieldPhoto" x1="0" y1="1" x2="1" y2="0">
        <stop offset="0" stop-color="#1f2f5a"/>
        <stop offset="0.45" stop-color="#8d8f94"/>
        <stop offset="0.75" stop-color="#b59a78"/>
        <stop offset="1" stop-color="#d9dbe0"/>
      </linearGradient>
    </defs>
    <polygon points="1200,436 1200,848 685,848" fill="url(#fieldPhoto)"/>
  </svg>

  <h2 class="heading heading--residential">Residential<br>Rooftop PV</h2>
  <ul class="list list--arrow list--residential on-dark">
    <li>System sizes from 2.4kW to 12kW</li>
    <li>DIY Packages available</li>
    <li>Referral Bonus - 250$ for any successful solar referral</li>
    <li>Offset some or all of your energy use</li>
    <li>Electric Vehicle Charging Systems</li>
    <li>Fully insured</li>
    <li>25 Year system life</li>
    <li>Can raise value of your home by up to $20,000</li>
    <li>Extends the life of your roof</li>
    <li>100$ donation to a local charity as part of any solar install.</li>
  </ul>

  <ul class="list list--arrow list--offers on-light">
    <li>One free solar panel if ordered within one week of your birthday</li>
    <li>We offer financing.&nbsp; Finance a solar system with 20% down and you will be saving money immediately.&nbsp; Transfer the loan to your mortgage and increase your savings.</li>
    <li>Selling your house and love your solar? We will relocate the system to your new home for a small fee.</li>
  </ul>

  <h2 class="heading heading--rv">RV Solar</h2>
  <ol class="list list--numbered list--rv on-light">
    <li>DIY 300W package from 500$.&nbsp; 600W package from 700$</li>
    <li>Installation services available</li>
    <li>Keeps your batteries charged</li>
    <li>No longer deal with dead batteries</li>
    <li>Become the envy of all campers!</li>
    <li>Never have a dead cell phone battery again.</li>
  </ol>

  <h2 class="heading heading--facts">Some Facts<br>On Solar</h2>
  <ul class="list list--arrow list--facts on-light">
    <li>Alberta is the sunniest province in Canada and comparable to Florida</li>
    <li>Systems are designed to last 25 years but operate for as long as 40 years</li>
    <li>Virtually no maintenance required!</li>
    <li>How your power bill works.</li>
  </ul>

  <ul class="list list--arrow list--multi on-dark">
    <li>Protect yourself from rising power costs</li>
    <li>Not everyone can have solar.&nbsp; Once 30-40% of the market has solar, utilities will not allow all solar systems to be installed.</li>
    <li>Dispel the snow myth: Snow only reduces a systems output by 5-8% over the course of a year. This is because our sunny hours are mostly made up in the longer summer days.</li>
    <li>Solar panels are nearly indestructible. Hail cannot damage a solar panel.</li>
    <li>Any extra power generated in the summer is sold back to the grid as a credit on your bill.</li>
  </ul>

  <h2 class="heading heading--multi">Multi Purpose<br>Solar Power</h2>

</main>
</body>
</html>
```